Billboard design - consider what a billboard is

Design a billboard using my logo - Billboard is 6m x 3m
A Billboard is advertising for my company that is on a big sign.

Has to be clean and easy to read, and ideally highlights that we are Residential and Commercial builders.

Keep it clean and easy to read

The contact number for the board is

022 583 7092
www.harbourframeworks.co.nz
info@harbourframeworks.co.nz

Doesnt have to have all contact details if it doesnt fit

Has to catch peoples attention to contact us if they need a builder

Can you please change the sign to be all white writing, with black background ?
Updates

Please consider what a billboard is...

The design needs to be suitable for a billboard..

Target Market(s)

people driving past

Industry/Entity Type

Construction

Logo Text

Wellington Builder, website email address, contact number

Colors
0054AA
0677BA
7BADD7
CADEEF
E8F1F8

Requirements
Must have
• Easy to read
Nice to have
• easy to read, can clearly see contact details

```html
<!DOCTYPE html>
<html lang="en">
<head>
<meta charset="utf-8">
<title>Harbour Frameworks Billboard</title>
<link href="https://fonts.googleapis.com/css2?family=Fira+Sans:wght@700;800&family=Montserrat:wght@800&display=swap" rel="stylesheet">
<style>
  :root {
    --navy: #1351a3;
    --pale: #cfe1f2;
    --brand: #5b8bc9;
    --white: #ffffff;
    --page: #ffffff;
  }
  * { margin: 0; padding: 0; box-sizing: border-box; }
  html, body {
    width: 1196px;
    height: 1200px;
    overflow: hidden;
    background: var(--page);
  }
  .billboard {
    position: absolute;
    left: 40px;
    top: 321px;
    width: 1116px;
    height: 556px;
    font-family: "Fira Sans", Arial, sans-serif;
  }
  .headline-panel {
    position: absolute;
    left: 0; top: 0;
    width: 100%;
    height: 348px;
    background: var(--pale);
  }
  .brand {
    position: absolute;
    left: 54px;
    top: 118px;
    display: flex;
    align-items: center;
    gap: 22px;
    color: var(--brand);
    font-weight: 800;
    font-size: 70px;
    line-height: 0.98;
  }
  .brand-mark {
    width: 44px;
    height: 44px;
    background: var(--brand);
    flex: none;
  }
  .headline {
    position: absolute;
    right: 54px;
    color: var(--navy);
    font-weight: 800;
    line-height: 1;
    white-space: nowrap;
  }
  .headline.city { top: 17px; font-size: 95px; letter-spacing: 0.5px; }
  .headline.trade { top: 114px; font-size: 109px; }
  .services {
    position: absolute;
    right: 54px;
    width: 444px;
    color: var(--navy);
    font-weight: 700;
    font-size: 39px;
    line-height: 1;
    white-space: nowrap;
  }
  .services.first {
    top: 240px;
    display: flex;
    align-items: center;
    justify-content: space-between;
  }
  .services.second { top: 283px; text-align: right; }
  .services .bar {
    width: 62px;
    height: 20px;
    background: var(--navy);
  }
  .contact-band {
    position: absolute;
    left: 0; top: 348px;
    width: 100%;
    height: 208px;
    background: var(--navy);
    color: var(--white);
    text-align: center;
  }
  .phone {
    position: absolute;
    left: 0; right: 0;
    top: 18px;
    font-family: "Montserrat", Arial, sans-serif;
    font-weight: 800;
    font-size: 86px;
    line-height: 1;
    word-spacing: 12px;
  }
  .web-row {
    position: absolute;
    left: 58px; right: 58px;
    top: 112px;
    display: flex;
    align-items: center;
    gap: 14px;
  }
  .web-row .rule {
    flex: 1;
    height: 4px;
    background: var(--white);
  }
  .website {
    font-weight: 700;
    font-size: 41px;
    line-height: 1;
  }
  .email {
    position: absolute;
    left: 0; right: 0;
    top: 160px;
    font-weight: 700;
    font-size: 29px;
    line-height: 1;
  }
</style>
</head>
<body>
  <div class="billboard">
    <section class="headline-panel">
      <div class="brand">
        <span class="brand-mark"></span>
        <span class="brand-name">Harbour<br>Frameworks</span>
      </div>
      <h1 class="headline city">WELLINGTON</h1>
      <h2 class="headline trade">BUILDER</h2>
      <p class="services first"><span class="bar"></span>RESIDENTIAL &amp;<span class="bar"></span></p>
      <p class="services second">COMMERCIAL BUILDERS</p>
    </section>
    <section class="contact-band">
      <p class="phone">022 583 7092</p>
      <div class="web-row">
        <span class="rule"></span>
        <span class="website">www.harbourframeworks.co.nz</span>
        <span class="rule"></span>
      </div>
      <p class="email">info@harbourframeworks.co.nz</p>
    </section>
  </div>
</body>
</html>
```